Silver Heron Coffee Bean Labels

We need a label for a new brand of coffee that we are selling in Portland, Oregon (Coffee Capital). Our company has no current online presence but have some great roasting techniques. We will be roasting our own coffee beans from throughout the world and selling them immediately after roasting causing a super fresh and high quality product.

We will be packaging in brown kraft bags: 3 3/8 X 2.5 x 7.75 inches which is standard for coffee beans.

Also notice on that sample the blue section in the middle has the product name. We want to also make it so that there is a consistent area that we can print OVER the label the name or blend of the coffee.

Our company is called Silver Heron Coffee Roasters. We will want to put silverheronroasters.example on the label someplace (we dont have a site yet but will by launch).

We need to incorporate A Silver Heron into the design. No preferences yet on the style of it.

We want to be a super-premium brand. Sort of like MicroBrew beers. We will sell at Farmers Markets, online, and directly into stores. Image is very important to us.

Labels should be about 3" wide and about 3.75" high.. Perhaps higher if a cool design justifies the height. Again we will be using a brown kraft bag (like grocery bag color) as shown on the sample.

SEE ATTACHED SEVERAL INTERESTING DESIGNS

Target Market(s)

Foodies, Yuppie, Coffee Snob

Industry/Entity Type

It Company

Requirements
Must have
• Location for the product Name to go onto it... We want to use the same labels for our full line. Just printing over it something like "Italian Roast" and a line below saying something like "Bold, Nutty Flavor, blah blah"

Should not have
• Clunkey looking old fonts or things that look homemade.

```html
<!DOCTYPE html>
<html lang="en">
<head>
<meta charset="utf-8">
<title>Silver Heron Coffee Roasters – Bag Label</title>
<link rel="stylesheet" href="https://fonts.googleapis.com/css2?family=Archivo:wght@600;700;800;900&display=swap">
<style>
  :root {
    --page: #ebe6de;
    --label: #c4ae90;
    --ink: #4a2f20;
    --rule: #4a3323;
    --name-field: #f3eee9;
    --coffee: #c85a2c;
    --roasters: #b86d4c;
    --fresh: #a65a48;
    --high: #5b3a29;
  }
  * { margin: 0; padding: 0; box-sizing: border-box; }
  html, body {
    width: 691px;
    height: 1200px;
    overflow: hidden;
    background: var(--page);
  }
  .canvas {
    position: relative;
    width: 691px;
    height: 1200px;
    overflow: hidden;
  }
  .label {
    position: absolute;
    left: 55px;
    top: 131px;
    width: 580px;
    height: 938px;
    display: block;
    font-family: "Archivo", "Helvetica Neue", Arial, sans-serif;
  }
  .label__ground { fill: var(--label); stroke: var(--rule); stroke-width: 10; }
  .rule { fill: var(--rule); }
  .name-field { fill: var(--name-field); }
  .site-url { fill: var(--ink); font-size: 13px; font-weight: 800; }
  .brand-first { fill: var(--ink); font-size: 139px; font-weight: 900; }
  .brand-second { fill: var(--ink); font-size: 61px; font-weight: 900; }
  .side-coffee { fill: var(--coffee); font-size: 146px; font-weight: 900; }
  .side-roasters { fill: var(--roasters); font-size: 68px; font-weight: 800; }
  .claim-super { fill: var(--fresh); font-size: 104px; font-weight: 900; }
  .claim-fresh { fill: var(--fresh); font-size: 65px; font-weight: 800; }
  .brand-mark { fill: var(--ink); font-size: 32px; font-weight: 900; }
  .claim-high { fill: var(--high); font-size: 114px; font-weight: 900; }
  .claim-quality { fill: var(--high); font-size: 42px; font-weight: 900; }
</style>
</head>
<body>
  <main class="canvas">
    <svg class="label" viewBox="0 0 580 938" width="580" height="938" aria-label="Silver Heron Coffee Roasters label">
      <rect class="label__ground" x="5" y="5" width="570" height="928"/>

      <text class="site-url" x="59" y="40" textLength="451" lengthAdjust="spacingAndGlyphs">www.SILVERHERONROASTERS.example</text>
      <rect class="rule" x="21" y="58" width="538" height="6"/>

      <text class="brand-first" x="65" y="187" textLength="450" lengthAdjust="spacingAndGlyphs">SILVER</text>
      <text class="brand-second" x="65" y="259" textLength="445" lengthAdjust="spacingAndGlyphs">HERON</text>
      <rect class="rule" x="21" y="273" width="538" height="6"/>

      <rect class="name-field" x="28" y="307" width="526" height="98" rx="14" aria-label="Blend name print area"/>

      <text class="side-coffee" transform="translate(140 874) rotate(-90)" x="0" y="0" textLength="449" lengthAdjust="spacingAndGlyphs">COFFEE</text>
      <text class="side-roasters" transform="translate(206 874) rotate(-90)" x="0" y="0" textLength="437" lengthAdjust="spacingAndGlyphs">ROASTERS</text>

      <text class="claim-super" x="253" y="515" textLength="289" lengthAdjust="spacingAndGlyphs">SUPER</text>
      <text class="claim-fresh" x="259" y="568" textLength="283" lengthAdjust="spacingAndGlyphs">FRESH</text>

      <text class="brand-mark" x="277" y="667" textLength="240" lengthAdjust="spacingAndGlyphs">SILVER HERON</text>

      <text class="claim-high" x="262" y="821" textLength="271" lengthAdjust="spacingAndGlyphs">HIGH</text>
      <text class="claim-quality" x="262" y="874" textLength="271" lengthAdjust="spacingAndGlyphs">QUALITY</text>
    </svg>
  </main>
</body>
</html>
```